Kettering Plumbing & Heating Limited needs a service and maintenance contract document design

Kettering Plumbing & Heating Limited are a well established family owned and operated company.

We currently offer installation, service and repair services for gas, plumbing, heating and electrical work. We wish to offer service and maintenance plans for plumbing, heating and electrical for our domestic clients in the UK. We would like the brochure to incorporate our company logo and colours, and reflect the reliable, quality, 5 star service we offer our clients.
I have attached a brochure that a friends company uses to give a good idea of the structure of the plans we wish to offer. We want to give our customers a choice in what packages best suit their needs. However, the pricing structure and certain elements/content of what we offer will be slightly different due to our geographical location.

We would like to have the basic structure of the brochure put in place and the
text content editable to our specific needs. Looking for advice on this but we do have Acrobat DC if we need to edit the text ourselves?

We use our logo with "KETTERS" in white over a grey backgound.

Our website is - www.ketters.plumbing
Facebook and twitter handle is - @KettersHeating

Target Market(s)

UK domestic plumbing, heating, natural gas, LPG and electrical market. Both private homeowners and landlords. Please see both the domestic and landlord document files attached for an idea on what we'd like.

Colors

Designer to choose colors to be used in the design.

Requirements
Must have
• Would like the finished design to incorporate the branding and colours we already use. Professional, Contemporary designs that will stand out above our competition.
• The content of the brochures MUST be very similar in structure to the files I’ve attached to the brief.
• We are having many designs submitted that are just copying our website content. This is not what we are asking for.
• I would like the icons etc to be redesigned so they are ours and not copied.
• Please also see the Landlords brochure attached to the brief. We would like this to be a separate document but to reflect the same design as the homeowner design you submit.
• The content of the documents will need to be re worded for our own use but I'm happy to change this once the design element is in place.
• A4 sized pages as per the example I've attached
• Must be able to attach the document to our website for clients to download.
Nice to have
• A4 sized pages as per the examples I've attached
Should not have
• Please DO NOT copy the content from our website to create our service plan brochures. This is not what we are after. As above, we need the brochures to be like the ones we've provided but made to fit our brand.
• Thank you

```html
<!DOCTYPE html>
<html lang="en">
<head>
<meta charset="utf-8">
<title>Ketters – Home Comfort plans at a glance</title>
<link href="https://fonts.googleapis.com/css2?family=PT+Sans:wght@400;700&family=PT+Sans+Narrow:wght@700&family=Caveat:wght@500&display=swap" rel="stylesheet">
<style>
  :root{
    --backdrop:#3c3c3e;
    --paper:#ffffff;
    --ink:#2b2b2b;
    --ink-soft:#6b6b6b;
    --orange:#f7941d;
    --orange-deep:#f15a24;
    --white:#ffffff;
    --card-foundation:#e5dbe0;
    --card-heating:#f5cbbd;
    --card-water:#b9cdea;
    --card-energy:#fde3c7;
    --card-gas:#e1d7db;
    --label-foundation:#8b8086;
    --label-heating:#d71920;
    --label-water:#1e9bd7;
    --label-energy:#ea5a28;
    --label-gas:#7a7a7a;
    --black-top:#3d3d3d; --black-front:#1c1c1c; --black-side:#050505;
    --red-top:#ea3a40; --red-front:#d71920; --red-side:#a3121a;
    --blue-top:#44b9ea; --blue-front:#1e9bd7; --blue-side:#13739f;
    --orange-top:#f3703f; --orange-front:#e9562a; --orange-side:#b4401b;
    --grey-top:#adadad; --grey-front:#8e8e8e; --grey-side:#6a6a6a;
  }
  *{margin:0;padding:0;box-sizing:border-box}
  html,body{width:1200px;height:866px;overflow:hidden;background:var(--backdrop)}
  body{font-family:"PT Sans",sans-serif;color:var(--ink)}
  .stage{position:relative;width:1200px;height:866px;background:var(--backdrop)}
  .page{position:absolute;top:41px;width:556px;height:785px;background:var(--paper)}
  .page--left{left:40px}
  .page--right{left:604px}

  .tagline{position:absolute;left:48px;top:26px;font-family:"Caveat",cursive;font-size:30px;color:#4a4a4a}
  .brand{position:absolute;left:346px;top:30px;display:flex;align-items:center;gap:9px}
  .brand__dot{width:30px;height:30px;border-radius:50%;background:var(--orange-deep)}
  .brand__name{font-family:"PT Sans",sans-serif;font-weight:700;font-size:30px;letter-spacing:1px;color:#333}

  .panel{position:absolute;top:69px;height:663px}
  .panel--left{left:19px;width:537px;border-radius:16px 0 0 16px;
    background:linear-gradient(90deg,var(--orange-deep) 0%,#f36f22 45%,var(--orange) 85%)}
  .panel--right{left:0;width:536px;border-radius:0 16px 16px 0;background:var(--orange)}

  .headline{position:absolute;left:19px;top:20px;font-family:"PT Sans Narrow",sans-serif;font-weight:700;
    font-size:62px;line-height:61px;color:var(--white);letter-spacing:-0.5px}
  .intro{position:absolute;left:17px;top:404px;width:345px;color:var(--white)}
  .intro p{font-size:11.6px;line-height:18.4px;margin-bottom:9px;font-weight:400;opacity:.95}
  .intro p.intro__lead{font-weight:700;font-size:11.8px}

  .card{position:absolute;border-radius:10px;text-align:center}
  .card__title{display:block;font-size:8.6px;padding-top:10px;white-space:nowrap}
  .card svg{position:absolute;left:14px;overflow:visible}
  .card--foundation{background:var(--card-foundation)} .card--foundation .card__title{color:var(--label-foundation)}
  .card--heating{background:var(--card-heating)} .card--heating .card__title{color:var(--label-heating)}
  .card--water{background:var(--card-water)} .card--water .card__title{color:var(--label-water)}
  .card--energy{background:var(--card-energy)} .card--energy .card__title{color:var(--label-energy)}
  .card--gas{background:var(--card-gas)} .card--gas .card__title{color:var(--label-gas)}

  .section-label{position:absolute;left:398px;top:264px;font-size:12px;color:var(--white)}
  .rule{position:absolute;top:283px;height:1px;background:var(--white)}

  .price{font-family:"PT Sans",sans-serif;font-weight:700;font-size:17px;fill:var(--white);
    stroke:rgba(0,0,0,.28);stroke-width:2px;paint-order:stroke;text-anchor:middle}
  .label{font-family:"PT Sans",sans-serif;font-size:8px;fill:var(--white);text-anchor:middle}

  .promo{position:absolute;left:34px;top:448px;width:400px;color:var(--ink)}
  .promo__script{font-family:"Caveat",cursive;font-size:32px;line-height:34px;color:#1f1f1f}
  .promo__heading{font-size:19px;font-weight:700;line-height:24px;margin-bottom:10px;color:#1f1f1f}
  .promo p{font-size:8.4px;line-height:12px;margin-bottom:10px;width:350px}
  .promo h3{font-size:9.6px;font-weight:700;margin-bottom:10px}

  .package{position:absolute;left:410px;top:24px;width:115px;height:625px;background:var(--card-gas);border-radius:10px}
  .package__title{position:absolute;left:2px;top:10px;width:111px;text-align:center;font-size:7.1px;letter-spacing:-0.1px;white-space:nowrap;color:var(--label-energy)}
  .package__text{position:absolute;left:12px;top:25px;width:96px;font-size:7.3px;line-height:12px;color:var(--ink)}
  .package__step{position:absolute;left:0;width:115px;text-align:center;font-size:7.6px;white-space:nowrap}
  .package__step--foundation{color:var(--ink)}
  .package__step--heating{color:var(--label-heating)}
  .package__step--water{color:var(--label-water)}
  .package__step--energy{color:var(--label-energy)}
  .package__note{position:absolute;left:10px;top:505px;width:100px;font-size:7px;line-height:9.6px;color:var(--ink-soft)}
  .package svg{position:absolute;left:15px;overflow:visible}
</style>
</head>
<body>
<svg width="0" height="0" style="position:absolute" aria-hidden="true">
  <defs>
    <g id="cap-black"><polygon points="0,18 88,2 96,14 8,30" style="fill:var(--black-top)"/></g>
    <g id="tier-black"><polygon points="0,18 8,30 8,56 0,44" style="fill:var(--black-side)"/><polygon points="8,30 96,14 96,40 8,56" style="fill:var(--black-front)"/><circle cx="18" cy="42" r="4" fill="none" stroke="#fff" stroke-width="1"/></g>
    <g id="cap-red"><polygon points="0,18 88,2 96,14 8,30" style="fill:var(--red-top)"/></g>
    <g id="tier-red"><polygon points="0,18 8,30 8,56 0,44" style="fill:var(--red-side)"/><polygon points="8,30 96,14 96,40 8,56" style="fill:var(--red-front)"/><circle cx="18" cy="42" r="4" fill="none" stroke="#fff" stroke-width="1"/></g>
    <g id="cap-blue"><polygon points="0,18 88,2 96,14 8,30" style="fill:var(--blue-top)"/></g>
    <g id="tier-blue"><polygon points="0,18 8,30 8,56 0,44" style="fill:var(--blue-side)"/><polygon points="8,30 96,14 96,40 8,56" style="fill:var(--blue-front)"/><circle cx="18" cy="42" r="4" fill="none" stroke="#fff" stroke-width="1"/></g>
    <g id="cap-orange"><polygon points="0,18 88,2 96,14 8,30" style="fill:var(--orange-top)"/></g>
    <g id="tier-orange"><polygon points="0,18 8,30 8,56 0,44" style="fill:var(--orange-side)"/><polygon points="8,30 96,14 96,40 8,56" style="fill:var(--orange-front)"/><circle cx="18" cy="42" r="4" fill="none" stroke="#fff" stroke-width="1"/></g>
    <g id="cap-grey"><polygon points="0,18 88,2 96,14 8,30" style="fill:var(--grey-top)"/></g>
    <g id="tier-grey"><polygon points="0,18 8,30 8,56 0,44" style="fill:var(--grey-side)"/><polygon points="8,30 96,14 96,40 8,56" style="fill:var(--grey-front)"/><circle cx="18" cy="42" r="4" fill="none" stroke="#fff" stroke-width="1"/></g>
  </defs>
</svg>

<main class="stage">
  <section class="page page--left">
    <div class="tagline">We care</div>
    <div class="brand"><span class="brand__dot"></span><span class="brand__name">KETTERS</span></div>
    <div class="panel panel--left">
      <h1 class="headline">The<br>Home<br>Comfort<br>plans<br>at a<br>glance</h1>
      <div class="intro">
        <p>The diagrams to the right illustrate the different plans and combination packs available from Home Comfort, and how they might work together.</p>
        <p class="intro__lead">Our Boiler Service plan will always form the foundation of your chosen package. After that, you’re free to add as few or as many plans and/or combination packs as you like, to create a completely bespoke package that meets your household’s needs.</p>
        <p>The monthly cost for each plan and combination pack is shown in the diagrams to the right. To work out how much you’ll need to pay in total for each month, simply add up the costs that apply to your chosen plans and/or combination packs.</p>
      </div>

      <div class="card card--foundation" style="left:270px;top:24px;width:115px;height:197px">
        <span class="card__title">Foundation Plan</span>
        <svg style="top:24px" width="88" height="53" viewBox="0 0 100 60">
          <use href="#tier-black"/><use href="#cap-black"/>
          <text class="price" transform="translate(50,22) rotate(-10.3)">£5</text>
          <text class="label" transform="translate(57,45) rotate(-10.3)">Boiler service</text>
        </svg>
      </div>

      <div class="card card--heating" style="left:398px;top:24px;width:115px;height:197px">
        <span class="card__title">Heating Maintenance Plans</span>
        <svg style="top:24px" width="88" height="160" viewBox="0 0 100 182">
          <use href="#tier-red"/><use href="#cap-red"/>
          <text class="price" transform="translate(50,22) rotate(-10.3)">£6</text>
          <text class="label" transform="translate(57,45) rotate(-10.3)">Boiler</text>
          <g transform="translate(0,62)">
            <use href="#tier-red"/><use href="#cap-red"/>
            <text class="price" transform="translate(50,22) rotate(-10.3)">£3</text>
            <text class="label" transform="translate(57,45) rotate(-10.3)">Controls</text>
          </g>
          <g transform="translate(0,124)">
            <use href="#tier-red"/><use href="#cap-red"/>
            <text class="price" transform="translate(50,22) rotate(-10.3)">£3</text>
            <text class="label" transform="translate(57,45) rotate(-10.3)">Central heating</text>
          </g>
        </svg>
      </div>

      <div class="section-label">Our Combination Packs</div>
      <div class="rule" style="left:398px;width:139px"></div>

      <div class="card card--heating" style="left:398px;top:298px;width:115px;height:121px">
        <span class="card__title">Heating Twin Pack</span>
        <svg style="top:24px" width="88" height="74" viewBox="0 0 100 84">
          <use href="#cap-red"/><use href="#tier-red"/>
          <g transform="translate(0,26)"><use href="#tier-red"/></g>
          <text class="price" transform="translate(50,22) rotate(-10.3)">£5</text>
          <text class="label" transform="translate(57,45) rotate(-10.3)">Controls</text>
          <text class="label" transform="translate(57,71) rotate(-10.3)">Central heating</text>
        </svg>
      </div>

      <div class="card card--heating" style="left:398px;top:454px;width:115px;height:150px">
        <span class="card__title">Heating Triple Pack</span>
        <svg style="top:24px" width="88" height="95" viewBox="0 0 100 108">
          <use href="#cap-red"/><use href="#tier-red"/>
          <g transform="translate(0,26)"><use href="#tier-red"/></g>
          <g transform="translate(0,52)"><use href="#tier-red"/></g>
          <text class="price" transform="translate(50,22) rotate(-10.3)">£10</text>
          <text class="label" transform="translate(57,45) rotate(-10.3)">Boiler</text>
          <text class="label" transform="translate(57,71) rotate(-10.3)">Controls</text>
          <text class="label" transform="translate(57,97) rotate(-10.3)">Central heating</text>
        </svg>
      </div>
    </div>
  </section>

  <section class="page page--right">
    <div class="brand"><span class="brand__dot"></span><span class="brand__name">KETTERS</span></div>
    <div class="panel panel--right">
      <div class="card card--water" style="left:23px;top:24px;width:116px;height:197px">
        <span class="card__title">Water Maintenance Plans</span>
        <svg style="top:24px" width="88" height="108" viewBox="0 0 100 120">
          <use href="#tier-blue"/><use href="#cap-blue"/>
          <text class="price" transform="translate(50,22) rotate(-10.3)">£3</text>
          <text class="label" transform="translate(57,45) rotate(-10.3)">Plumbing</text>
          <g transform="translate(0,62)">
            <use href="#tier-blue"/><use href="#cap-blue"/>
            <text class="price" transform="translate(50,22) rotate(-10.3)">£3</text>
            <text class="label" transform="translate(57,45) rotate(-10.3)">Drains</text>
          </g>
        </svg>
      </div>

      <div class="card card--energy" style="left:152px;top:24px;width:116px;height:197px">
        <span class="card__title">Energy Maintenance Plans</span>
        <svg style="top:24px" width="88" height="108" viewBox="0 0 100 120">
          <use href="#tier-orange"/><use href="#cap-orange"/>
          <text class="price" transform="translate(50,22) rotate(-10.3)">£2</text>
          <text class="label" transform="translate(57,45) rotate(-10.3)">Gas pipe</text>
          <g transform="translate(0,62)">
            <use href="#tier-orange"/><use href="#cap-orange"/>
            <text class="price" transform="translate(50,22) rotate(-10.3)">£4</text>
            <text class="label" transform="translate(57,45) rotate(-10.3)">Electrics</text>
          </g>
        </svg>
      </div>

      <div class="card card--gas" style="left:281px;top:24px;width:116px;height:197px">
        <span class="card__title">Gas Fire Plan</span>
        <svg style="top:24px" width="88" height="53" viewBox="0 0 100 60">
          <use href="#tier-grey"/><use href="#cap-grey"/>
          <text class="price" transform="translate(50,22) rotate(-10.3)">£5</text>
          <text class="label" transform="translate(57,45) rotate(-10.3)">Gas fire</text>
        </svg>
      </div>

      <div class="rule" style="left:0;width:268px"></div>

      <div class="card card--water" style="left:23px;top:298px;width:116px;height:121px">
        <span class="card__title">Water Pack</span>
        <svg style="top:24px" width="88" height="74" viewBox="0 0 100 84">
          <use href="#cap-blue"/><use href="#tier-blue"/>
          <g transform="translate(0,26)"><use href="#tier-blue"/></g>
          <text class="price" transform="translate(50,22) rotate(-10.3)">£5</text>
          <text class="label" transform="translate(57,45) rotate(-10.3)">Plumbing</text>
          <text class="label" transform="translate(57,71) rotate(-10.3)">Drains</text>
        </svg>
      </div>

      <div class="card card--energy" style="left:152px;top:298px;width:116px;height:121px">
        <span class="card__title">Energy Pack</span>
        <svg style="top:24px" width="88" height="74" viewBox="0 0 100 84">
          <use href="#cap-orange"/><use href="#tier-orange"/>
          <g transform="translate(0,26)"><use href="#tier-orange"/></g>
          <text class="price" transform="translate(50,22) rotate(-10.3)">£5</text>
          <text class="label" transform="translate(57,45) rotate(-10.3)">Gas pipe</text>
          <text class="label" transform="translate(57,71) rotate(-10.3)">Electrics</text>
        </svg>
      </div>

      <div class="promo">
        <div class="promo__script">Save money</div>
        <h2 class="promo__heading">with Combination Packs</h2>
        <p>As you can see, we’ve put some of our plans together to create money-saving combination packs, which cost less per month than buying each plan individually. You’ll find out more about these on pages 8, 9, 11 and 13.</p>
        <h3>Building your Home Comfort package</h3>
        <p>As long as your package includes our Boiler Service plan, you’re free to mix and match our other plans and combination packs as you choose, to create your very own, customised Home Comfort package.</p>
      </div>

      <aside class="package">
        <div class="package__title">The full Home Comfort Package</div>
        <p class="package__text">If you choose the full Home Comfort package as shown in the diagram below, your monthly payment to us will be just <b>£25 per month.</b></p>
        <div class="package__step package__step--foundation" style="top:96px">Foundation Plan</div>
        <svg style="top:108px" width="84" height="50" viewBox="0 0 100 60">
          <use href="#tier-black"/><use href="#cap-black"/>
          <text class="price" transform="translate(50,22) rotate(-10.3)">£5</text>
          <text class="label" transform="translate(57,45) rotate(-10.3)">Boiler service</text>
        </svg>
        <div class="package__step package__step--heating" style="top:169px">+ Heating Triple Pack</div>
        <svg style="top:182px" width="84" height="91" viewBox="0 0 100 108">
          <use href="#cap-red"/><use href="#tier-red"/>
          <g transform="translate(0,26)"><use href="#tier-red"/></g>
          <g transform="translate(0,52)"><use href="#tier-red"/></g>
          <text class="price" transform="translate(50,22) rotate(-10.3)">£10</text>
          <text class="label" transform="translate(57,45) rotate(-10.3)">Boiler</text>
          <text class="label" transform="translate(57,71) rotate(-10.3)">Controls</text>
          <text class="label" transform="translate(57,97) rotate(-10.3)">Central heating</text>
        </svg>
        <div class="package__step package__step--water" style="top:300px">+ Water Pack</div>
        <svg style="top:312px" width="84" height="70" viewBox="0 0 100 84">
          <use href="#cap-blue"/><use href="#tier-blue"/>
          <g transform="translate(0,26)"><use href="#tier-blue"/></g>
          <text class="price" transform="translate(50,22) rotate(-10.3)">£5</text>
          <text class="label" transform="translate(57,45) rotate(-10.3)">Plumbing</text>
          <text class="label" transform="translate(57,71) rotate(-10.3)">Drains</text>
        </svg>
        <div class="package__step package__step--energy" style="top:402px">+ Energy Pack</div>
        <svg style="top:414px" width="84" height="70" viewBox="0 0 100 84">
          <use href="#cap-orange"/><use href="#tier-orange"/>
          <g transform="translate(0,26)"><use href="#tier-orange"/></g>
          <text class="price" transform="translate(50,22) rotate(-10.3)">£5</text>
          <text class="label" transform="translate(57,45) rotate(-10.3)">Gas pipe</text>
          <text class="label" transform="translate(57,71) rotate(-10.3)">Electrics</text>
        </svg>
        <p class="package__note">If you’d also like us to cover one or more gas fires in your home, you’ll need to add on a monthly cost of £5 per fire to this total.</p>
        <svg style="top:560px" width="84" height="50" viewBox="0 0 100 60">
          <use href="#tier-grey"/><use href="#cap-grey"/>
          <text class="price" transform="translate(50,22) rotate(-10.3)">£5</text>
          <text class="label" transform="translate(57,45) rotate(-10.3)">Gas fire</text>
        </svg>
      </aside>
    </div>
  </section>
</main>
</body>
</html>
```